Business Card Design

Vintage looking Hair Salon, where the customer service is 100%. We are based in a cottage. With shabby chic console tables and beautiful ornate mirrors..and rich brown leather cutting chairs. Chandeliers at the window, and a ornate patchwork sofa.
our clientele are 28years upwards.. Mums with small children.. Ladies that lunch, and men that want more than a barbers and are prepared to pay for our services.
I am looking for a classy business card.. That look expensive.. Where our initials WMP become a visual reference.. I was thinking of cream card initials in black on a embossed tarnished silver.. But I'm open to suggestion. I want,  need the design to be able to work with flyers price list ect.

Industry/Entity Type
Business
Contact Information for Business Card
Willow Mane Parlour
17 Fernbrook Lane
Dunmore Green
bN42 6QW
FB thewillowmaneparlour
Info@thewilowmaneparlour.co.uk
0208 761 5924

```html
<!DOCTYPE html>
<html lang="en">
<head>
<meta charset="utf-8">
<title>Willow Mane Parlour – Business Card</title>
<link href="https://fonts.googleapis.com/css2?family=Open+Sans:wght@400;700;800&display=swap" rel="stylesheet">
<style>
  :root {
    --backdrop: #8e99a6;
    --card: #f3f3f1;
    --band: #474747;
    --ink: #3a3a3a;
    --band-text: #ececec;
  }
  * { margin: 0; padding: 0; box-sizing: border-box; }
  html, body {
    width: 1200px;
    height: 675px;
    overflow: hidden;
    background: var(--backdrop);
    font-family: "Open Sans", Arial, sans-serif;
  }
  .stage {
    width: 1200px;
    height: 675px;
    display: flex;
    align-items: center;
    justify-content: center;
  }
  .card {
    position: relative;
    width: 920px;
    height: 540px;
    background: var(--card);
    box-shadow: 0 10px 30px rgba(0,0,0,0.18);
  }
  .brand {
    position: absolute;
    top: 0;
    left: 0;
    right: 0;
    height: 300px;
    display: flex;
    align-items: flex-end;
    justify-content: center;
    padding-bottom: 26px;
  }
  .brand-name {
    font-weight: 800;
    font-size: 40px;
    letter-spacing: 2px;
    text-transform: uppercase;
    color: var(--ink);
  }
  .contact-band {
    position: absolute;
    left: 0;
    right: 0;
    top: 300px;
    height: 128px;
    background: var(--band);
    display: flex;
    justify-content: space-between;
    align-items: center;
    padding: 0 56px 0 60px;
    color: var(--band-text);
    font-size: 19px;
  }
  .contact-column {
    display: flex;
    flex-direction: column;
    gap: 16px;
  }
  .contact-item {
    display: flex;
    align-items: center;
    gap: 18px;
    white-space: nowrap;
  }
  .contact-icon {
    width: 20px;
    height: 20px;
    flex: none;
    fill: none;
    stroke: var(--band-text);
    stroke-width: 1.6;
  }
  .contact-icon.solid { fill: var(--band-text); stroke: none; }
</style>
</head>
<body>
  <main class="stage">
    <section class="card">
      <header class="brand">
        <h1 class="brand-name">Willow Mane Parlour</h1>
      </header>

      <div class="contact-band">
        <div class="contact-column">
          <div class="contact-item">
            <svg class="contact-icon solid" viewBox="0 0 24 24" aria-hidden="true">
              <path d="M6.6 10.8a15.1 15.1 0 0 0 6.6 6.6l2.2-2.2a1 1 0 0 1 1-.25 11.4 11.4 0 0 0 3.6.6 1 1 0 0 1 1 1V20a1 1 0 0 1-1 1A17 17 0 0 1 3 4a1 1 0 0 1 1-1h3.5a1 1 0 0 1 1 1c0 1.25.2 2.45.6 3.6a1 1 0 0 1-.25 1z"/>
            </svg>
            <span class="contact-text">+44 0208 761 5924</span>
          </div>
          <div class="contact-item">
            <svg class="contact-icon" viewBox="0 0 24 24" aria-hidden="true">
              <circle cx="12" cy="12" r="9"/>
              <ellipse cx="12" cy="12" rx="4" ry="9"/>
              <line x1="3" y1="12" x2="21" y2="12"/>
              <line x1="5" y1="7" x2="19" y2="7"/>
              <line x1="5" y1="17" x2="19" y2="17"/>
            </svg>
            <span class="contact-text">www.thewillowmaneparlour.co.uk</span>
          </div>
        </div>

        <div class="contact-column">
          <div class="contact-item">
            <svg class="contact-icon solid" viewBox="0 0 24 24" aria-hidden="true">
              <path d="M3 6h18v1.2l-9 6-9-6z"/>
              <path d="M3 9.2l9 6 9-6V18H3z"/>
            </svg>
            <span class="contact-text">Info@thewilowmaneparlour.co.uk</span>
          </div>
          <div class="contact-item">
            <svg class="contact-icon solid" viewBox="0 0 24 24" aria-hidden="true">
              <path d="M12 2a7 7 0 0 0-7 7c0 5.2 7 13 7 13s7-7.8 7-13a7 7 0 0 0-7-7zm0 9.5A2.5 2.5 0 1 1 12 6.5a2.5 2.5 0 0 1 0 5z"/>
            </svg>
            <span class="contact-text">17 Fernbrook Lane Dunmore Green bN42 6QW</span>
          </div>
        </div>
      </div>
    </section>
  </main>
</body>
</html>
```